Book cover design project
Tides of the Evening
Male Multi-Orgasmic Masturbation
This is a self-help sex guide aimed at men who want to learn how to masturbate to orgasm as often as they want to.
Health
The target audience is all sexually active men.
I have in mind a simple one-color design (blue?) making use of the alliterating three M's of the subtitle (MMM), which will also echo the sound of a person having pleasure ("mmm..") and the visual image of a man lying on his back with his knees bent. No pictures of people or objects please, just subtle graphic suggestion!

```html
<!DOCTYPE html>
<html lang="en">
<head>
<meta charset="utf-8">
<title>Tides of the Evening — Book Cover</title>
<link rel="stylesheet" href="https://fonts.googleapis.com/css2?family=Mulish:wght@600;700&display=swap">
<style>
  :root {
    --page-bg: #ebebeb;
    --blue-deep: #0b1f6e;
    --blue-mid: #1f46b8;
    --blue-bright: #5f8fe6;
    --glow: #d6e4ff;
    --band: #0a1640;
    --ink: #ffffff;
    --rule: rgba(255,255,255,0.85);
  }
  * { margin: 0; padding: 0; box-sizing: border-box; }
  html, body {
    width: 1200px; height: 871px; overflow: hidden;
    background: var(--page-bg);
  }
  .stage { position: relative; width: 1200px; height: 871px; }
  .cover {
    position: absolute; left: 360px; top: 91px;
    width: 480px; height: 682px;
    overflow: hidden;
    background:
      radial-gradient(ellipse 55% 40% at 50% 18%, var(--glow) 0%, rgba(160,190,250,0.55) 30%, rgba(95,143,230,0) 70%),
      radial-gradient(ellipse 90% 75% at 50% 30%, var(--blue-bright) 0%, var(--blue-mid) 45%, var(--blue-deep) 100%);
    box-shadow: 0 3px 10px rgba(0,0,0,0.25);
    font-family: "Mulish", "Century Gothic", sans-serif;
    color: var(--ink);
    text-align: center;
  }
  .title {
    position: absolute; left: 0; right: 0; top: 160px;
    text-transform: uppercase;
    text-shadow: 0 3px 6px rgba(0,10,60,0.55);
    font-weight: 700;
    letter-spacing: 1px;
  }
  .title-line { display: block; line-height: 1; }
  .title-small { font-size: 60px; }
  .title-joiner {
    display: flex; align-items: center; justify-content: center;
    gap: 16px; font-size: 44px; margin: 22px 0 20px;
  }
  .title-joiner::before, .title-joiner::after {
    content: ""; width: 70px; height: 2px; background: var(--rule);
    box-shadow: 0 2px 4px rgba(0,10,60,0.4);
  }
  .title-large { font-size: 76px; }
  .subtitle-band {
    position: absolute; left: 0; right: 0; bottom: 0; height: 73px;
    background: var(--band);
    display: flex; align-items: center; justify-content: center;
    font-size: 17px; font-weight: 700; letter-spacing: 0.5px;
    text-transform: uppercase;
  }
</style>
</head>
<body>
  <div class="stage">
    <div class="cover">
      <h1 class="title">
        <span class="title-line title-small">Tides</span>
        <span class="title-line title-joiner">of the</span>
        <span class="title-line title-large">Evening</span>
      </h1>
      <div class="subtitle-band">Male Multi-Orgasmic Masturbation</div>
    </div>
  </div>
</body>
</html>
```